"leading industry company in search of a new web page"

we are searching for a clean, industry driven, engineered oriented web page design,

it need to be clean, and it need to have the chiefs company photo on the first page.
we are a mexican engineered company, we have 3 special sector specialties so in the front page we need to have a link to each one of these, and another one for CV "jobs" IM PUTING A COUPLE OD DESIGN IDEAL WITH OUR INFO SO YOU CAN PUT IT ALL TOGETHER

IM PUTING OUR LOGO AVAILABLE SO YOU CAN PUT IT IN THE PAGE

OUR WEB PAGE IS http://dravol.com.mx

Target Market(s)

INDUSTRY LIKES ENERGY AND PETROL
COMPANIES IN THE ENGINEERING BUSINESS

Industry/Entity Type

Industry

Requirements
Must have
• CLEAN DESIGN,
• HIRING AND CV DEDICATED MENU TAB
• THE 3 DIVISIONS OF THE COMPANY
• SOCIAL MEDIA ON THE BOTTOM "JUST PLAIN SOCIAL SQUARE AND PLAIN SOCIAL SQUARE"
Nice to have
• COHERENCE WITH THE LOGO COLORS

```html
<!DOCTYPE html>
<html lang="en">
<head>
<meta charset="utf-8">
<title>DRAVOL — Quality Engineering</title>
<link href="https://fonts.googleapis.com/css2?family=Arimo:wght@400;700&family=Pinyon+Script&display=swap" rel="stylesheet">
<style>
  :root {
    --black: #000;
    --white: #fff;
    --green: #6aa321;
    --green-light: #8cc63f;
    --red: #d62b45;
    --red-soft: #f3b8c2;
    --navy: #1d2a5a;
    --text: #111;
    --grey: #8a8a8a;
  }
  * { box-sizing: border-box; margin: 0; padding: 0; }
  html, body { width: 889px; height: 1200px; overflow: hidden; }
  body { position: relative; background: var(--white); font-family: "Arimo", Arial, sans-serif; color: var(--text); }

  .site-header { position: absolute; left: 0; top: 0; width: 889px; height: 115px; background: var(--black); }
  .brand { position: absolute; left: 36px; top: 18px; display: flex; align-items: center; gap: 14px; }
  .brand-mark { width: 70px; height: 70px; border-radius: 50%; background: #8d8d8d; }
  .brand-name { font-size: 58px; font-weight: 700; color: var(--red); letter-spacing: 1px; line-height: 1; }
  .account-links { position: absolute; right: 77px; top: 15px; color: var(--white); font-size: 14px; }
  .main-nav { position: absolute; right: 76px; top: 71px; color: var(--white); font-size: 14px; letter-spacing: .3px; }
  .sep { margin: 0 6px; }

  .rule { position: absolute; left: 0; width: 889px; }
  .rule-top { top: 117px; height: 7px; border-top: 4px solid var(--green-light); border-bottom: 2px solid var(--white); background: var(--green); }
  .rule-foot { top: 1113px; height: 9px; border-top: 4px solid var(--green-light); border-bottom: 2px solid var(--white); background: var(--green); }

  .hero { position: absolute; left: 0; top: 124px; width: 889px; height: 488px;
    background: linear-gradient(180deg, #2f5e96 0%, #5d8cc0 35%, #c8d6e2 52%, #6f8398 60%, #1a3a68 70%, #0d2852 100%); }
  .hero-title { position: absolute; left: 116px; top: 22px; width: 690px; color: var(--white); font-size: 22px; font-weight: 700; line-height: 23px; text-transform: uppercase; }
  .slider-dots { position: absolute; left: 364px; top: 349px; width: 177px; height: 32px; background: rgba(0,0,0,.45); }

  .division { position: absolute; top: 506px; width: 238px; height: 288px; border: 1px solid #e8e8e8;
    background: linear-gradient(180deg, var(--red) 0%, #e16a7e 45%, var(--red-soft) 70%, var(--white) 100%); }
  .division h2 { position: absolute; left: 11px; top: 12px; color: var(--white); font-size: 15px; font-weight: 400; white-space: nowrap; }
  .division h2 span { font-family: "Pinyon Script", cursive; font-size: 24px; margin-left: 3px; }
  .division-photo { position: absolute; left: 11px; top: 53px; width: 216px; height: 105px; }
  .division p { position: absolute; left: 12px; top: 168px; width: 214px; font-size: 6.2px; line-height: 11px; color: var(--navy); text-align: justify; }
  .read-more { position: absolute; right: 11px; bottom: 14px; width: 53px; height: 19px; border-radius: 4px; background: var(--green); color: var(--white); font-size: 7px; line-height: 19px; text-align: center; }
  .div-industrial { left: 69px; }
  .div-verification { left: 326px; }
  .div-admin { left: 582px; }

  .welcome { position: absolute; left: 71px; top: 804px; width: 493px; }
  .welcome h3, .hiring h3 { font-size: 16px; font-weight: 700; margin-bottom: 10px; }
  .welcome p { font-size: 13px; line-height: 12.5px; text-align: justify; margin-bottom: 12px; }

  .hiring { position: absolute; left: 583px; top: 804px; width: 208px; }
  .hiring-form { height: 186px; padding: 15px 14px 0; background: linear-gradient(180deg, var(--red) 0%, #e98c9b 60%, var(--white) 100%); }
  .field { background: var(--white); height: 24px; margin-bottom: 12px; font-size: 12.5px; padding: 5px 11px; }
  .field-letter { height: 46px; }
  .form-actions { display: flex; justify-content: space-between; font-size: 12.5px; padding: 0 1px; margin-top: -2px; }

  .partners { position: absolute; left: 0; top: 1048px; width: 889px; text-align: center; }
  .partners h4 { color: var(--navy); font-size: 13px; font-weight: 700; }
  .partner-badges { display: flex; justify-content: center; gap: 8px; margin-top: 10px; }
  .badge { width: 32px; height: 30px; background: #d9d9d9; }
  .badge.round { border-radius: 50%; background: #c9363f; }
  .badge.green { background: #5ba33a; width: 38px; }

  .site-footer { position: absolute; left: 0; top: 1122px; width: 889px; height: 78px; background: var(--black); color: var(--white); text-align: center; }
  .social { display: flex; justify-content: center; gap: 14px; margin-top: 9px; }
  .social span { width: 21px; height: 21px; border-radius: 4px; background: var(--green); }
  .footer-nav { font-size: 12px; margin-top: 8px; }
  .legal { font-size: 12px; margin-top: 3px; }
</style>
</head>
<body>
  <header class="site-header">
    <div class="brand"><span class="brand-mark"></span><span class="brand-name">dravol</span></div>
    <div class="account-links">Login<span class="sep">|</span>Sign up</div>
    <nav class="main-nav">HOME<span class="sep">|</span>NEWS<span class="sep">|</span>ABOUT US<span class="sep">|</span>SOLUTIONS<span class="sep">|</span>TECHNOLOGIES</nav>
  </header>
  <div class="rule rule-top"></div>

  <section class="hero" role="img" aria-label="Offshore oil platform standing in open sea under a blue sky">
    <h1 class="hero-title">DRAVOL provides premier consulting services for quality engineering in the nuclear, industrial and construction fields.</h1>
    <svg class="slider-dots" viewBox="0 0 177 32" aria-hidden="true">
      <circle cx="18" cy="13" r="8" fill="#1cb4ef"/>
      <circle cx="45" cy="13" r="8" fill="#6d6d6d"/>
      <circle cx="73" cy="13" r="8" fill="#6d6d6d"/>
      <circle cx="100" cy="13" r="8" fill="#6d6d6d"/>
      <circle cx="127" cy="13" r="8" fill="#6d6d6d"/>
      <circle cx="151" cy="13" r="8" fill="#6d6d6d"/>
    </svg>
  </section>

  <article class="division div-industrial">
    <h2>INDUSTRIAL<span>Division</span></h2>
    <div class="division-photo" role="img" aria-label="Refinery towers lit at night" style="background:linear-gradient(180deg,#1b1d3a,#3a3520 60%,#8a6a1c)"></div>
    <p>This department is responsible for all the activities that DRAVOL realizes during the application of non-destructive tests along the phases of manufacturing, construction, and mounting.</p>
    <span class="read-more">READ MORE</span>
  </article>
  <article class="division div-verification">
    <h2>VERIFICATION<span>Division</span></h2>
    <div class="division-photo" role="img" aria-label="Engineer in hard hat inspecting a panel on site" style="background:linear-gradient(180deg,#9aa6b4,#5f8a9e 55%,#c9ccd0)"></div>
    <p>DRAVOL is a verification unit approved by the Entidad Nacional de Acreditación Técnica to determine the compliance degree to Mexican Official Norms. The federal dependencies which have a approved us are Energy Oversight Board and Labor Standards Office.</p>
    <span class="read-more">READ MORE</span>
  </article>
  <article class="division div-admin">
    <h2>ADMINISTRATION<span>Division</span></h2>
    <div class="division-photo" role="img" aria-label="Business team meeting around a conference table" style="background:linear-gradient(180deg,#d8d6d2,#8a7c6c 60%,#4a3a2e)"></div>
    <p>DRAVOL is composed by a group of professionals of ample experience in the fields of technical assessment and management. Their main goal is to provide services so our clients can improve the quality and security of their products and installations.</p>
    <span class="read-more">READ MORE</span>
  </article>

  <section class="welcome">
    <h3>WELCOME</h3>
    <p>DRAVOL has performed since its founding in 1981 activities in quality engineering, material engineering, soldering certification, factory and field testing of equipment, as well as mexican norm and official mexican norm (NOM) certification.</p>
    <p>In 1986, DRAVOL participates in the Punta Serena Nuclear Power Plant Project of Comisión Regional de Energía (CRE) like a specialized and qualified enterprise, which carries out jobs regarding quality control, technical assistance and consulting, as well as supervision of testing and maintenance. Its intensive participation in the Nuclear Field, has allowed it to obtain a high grade of qualification and international projection into different industrial processes, mainly into the mechanical, electrical and instrumentation fields.</p>
    <p>DRAVOL has performing continuous services for the private and government's sectors. Its staff is constituted by trained technical professionals, qualified and certified by national and international norms and standards.</p>
  </section>

  <section class="hiring">
    <h3>WE ARE HIRING</h3>
    <div class="hiring-form">
      <div class="field">Full Name</div>
      <div class="field">Email Address</div>
      <div class="field field-letter">Cover Letter</div>
      <div class="form-actions"><span>Attach CV</span><span>SUBMIT</span></div>
    </div>
  </section>

  <section class="partners">
    <h4>Our Partners</h4>
    <div class="partner-badges">
      <span class="badge"></span><span class="badge green"></span><span class="badge round"></span>
    </div>
  </section>

  <div class="rule rule-foot"></div>
  <footer class="site-footer">
    <div class="social"><span aria-label="Social link"></span><span aria-label="Social link"></span></div>
    <nav class="footer-nav">HOME<span class="sep">|</span>NEWS<span class="sep">|</span>ABOUT US<span class="sep">|</span>SOLUTIONS<span class="sep">|</span>TECHNOLOGIES</nav>
    <div class="legal">©2013 DRAVOL | Terms of Use<span class="sep">|</span>Privacy Statement</div>
  </footer>
</body>
</html>
```